KTR Engineering Pty Ltd

I have already had Corvale welding and fabrication cards made , my business has changed too KTR engineering Pty Ltd so I need my logo changed on the cards
one side have my logo then the other side have what we do.
front side logo and details
owner /operator : Lachlan Meravic
email: ktr.works@ironvalemail.com
number: 0491537204
ABN: 47 261 538 902
ACN: 718 352 946
on back have in dot points what we do:
* structural steel erection
* precast panels
* site welding
*steel alteration & repair
* rigging & dogging
*labour hire
all details in breif

```html
<!DOCTYPE html>
<html lang="en">
<head>
<meta charset="utf-8">
<title>KTR Engineering Pty Ltd – Business Card</title>
<link href="https://fonts.googleapis.com/css2?family=Poppins:wght@400;500;600;700&display=swap" rel="stylesheet">
<style>
  :root {
    --navy: #122132;
    --rust: #94443a;
    --white: #ffffff;
    --ink: #1c2430;
    --stage: #bdbdbd;
  }
  * { box-sizing: border-box; margin: 0; padding: 0; }
  html, body { width: 1200px; height: 1200px; overflow: hidden; }
  body {
    background: var(--stage);
    font-family: "Poppins", sans-serif;
    position: relative;
  }
  .card {
    position: absolute;
    left: 229px;
    width: 742px;
    height: 424px;
    overflow: hidden;
  }
  .card--front { top: 136px; background: var(--white); }
  .card--back { top: 641px; background: var(--navy); }

  /* front */
  .name-tab {
    position: absolute; left: 0; top: 190px;
    width: 9px; height: 47px;
    background: var(--navy);
    border-radius: 0 5px 5px 0;
  }
  .owner { position: absolute; left: 24px; top: 186px; }
  .owner__name {
    font-size: 28px; font-weight: 600; color: var(--rust);
    line-height: 1.1; letter-spacing: 0.2px;
  }
  .owner__role { font-size: 17.5px; color: var(--ink); margin-top: 2px; }
  .contact { position: absolute; left: 25px; top: 256px; list-style: none; }
  .contact li {
    display: flex; align-items: center; gap: 6px;
    font-size: 17.5px; color: var(--ink); line-height: 20.5px;
  }
  .contact svg { width: 12px; height: 12px; flex: none; }
  .registry { position: absolute; left: 25px; top: 332px; }
  .registry p { font-size: 17.5px; color: var(--ink); line-height: 23.5px; }
  .registry b { font-weight: 500; color: var(--rust); }
  .band { position: absolute; left: 0; bottom: 0; width: 100%; height: 26px; }

  /* company name block */
  .brand { position: absolute; text-align: center; }
  .brand__name {
    font-weight: 700; letter-spacing: 0.5px; line-height: 1.15;
  }
  .brand__mark {
    display: inline-block; border-radius: 50%; background: var(--rust);
    vertical-align: middle; margin-right: 8px;
  }
  .brand__phone { font-weight: 600; letter-spacing: 1px; }
  .brand--front { left: 465px; top: 74px; width: 250px; }
  .brand--front .brand__name { font-size: 24px; color: var(--navy); }
  .brand--front .brand__mark { width: 14px; height: 14px; }
  .brand--front .brand__phone { font-size: 12px; color: var(--rust); margin-top: 6px; }
  .brand--back { left: 40px; top: 168px; width: 390px; }
  .brand--back .brand__name { font-size: 36px; color: var(--white); }
  .brand--back .brand__mark { width: 20px; height: 20px; }
  .brand--back .brand__phone { font-size: 17px; color: var(--rust); margin-top: 8px; }

  /* back */
  .services {
    position: absolute; left: 462px; top: 123px;
    width: 280px; height: 186px;
    background: var(--white);
    border-radius: 12px 0 0 12px;
    padding: 10px 0 0 15px;
  }
  .services__title {
    font-size: 17px; font-weight: 600; color: var(--rust); line-height: 22px;
  }
  .services__list { list-style: none; margin-top: 3px; }
  .services__list li {
    position: relative; padding-left: 15px;
    font-size: 17.5px; color: var(--ink); line-height: 23.6px;
  }
  .services__list li::before {
    content: ""; position: absolute; left: 0; top: 8px;
    width: 8px; height: 8px; border-radius: 50%; background: var(--rust);
  }
</style>
</head>
<body>

<section class="card card--front" aria-label="Card front">
  <div class="brand brand--front">
    <p class="brand__name"><span class="brand__mark"></span>KTR Engineering Pty Ltd</p>
    <p class="brand__phone">0491537204</p>
  </div>

  <span class="name-tab"></span>
  <div class="owner">
    <h1 class="owner__name">Lachlan Meravic</h1>
    <p class="owner__role">Owner &amp; Operator</p>
  </div>

  <ul class="contact">
    <li>
      <svg viewBox="0 0 12 12"><rect x="3" y="0.8" width="6" height="10.4" rx="1" fill="none" stroke="#94443a" stroke-width="1.4"/><circle cx="6" cy="9.3" r="0.7" fill="#94443a"/></svg>
      +049-1537-204
    </li>
    <li>
      <svg viewBox="0 0 12 12"><rect x="0.5" y="2.5" width="11" height="7.5" fill="#94443a"/><path d="M0.5 2.5 L6 7 L11.5 2.5" fill="none" stroke="#fff" stroke-width="1"/></svg>
      ktr.works@ironvalemail.com
    </li>
    <li>
      <svg viewBox="0 0 12 12" fill="none" stroke="#94443a" stroke-width="0.9"><circle cx="6" cy="6" r="5"/><ellipse cx="6" cy="6" rx="2.2" ry="5"/><path d="M1 6 H11 M2 3.5 H10 M2 8.5 H10"/></svg>
      www.ktrworks-eng.com
    </li>
  </ul>

  <div class="registry">
    <p><b>ACN</b> 718 352 946</p>
    <p><b>ABN</b> 47 261 538 902</p>
  </div>

  <svg class="band" viewBox="0 0 742 26" preserveAspectRatio="none">
    <polygon points="0,0 430,0 423,26 0,26" fill="#122132"/>
    <polygon points="435,0 742,0 742,26 428,26" fill="#94443a"/>
  </svg>
</section>

<section class="card card--back" aria-label="Card back">
  <div class="brand brand--back">
    <p class="brand__name"><span class="brand__mark"></span>KTR Engineering Pty Ltd</p>
    <p class="brand__phone">0491537204</p>
  </div>

  <div class="services">
    <h2 class="services__title">WHAT WE DO:</h2>
    <ul class="services__list">
      <li>structural steel erection</li>
      <li>precast panels</li>
      <li>site welding</li>
      <li>steel alteration &amp; repair</li>
      <li>rigging &amp; dogging</li>
      <li>labour hire</li>
    </ul>
  </div>
</section>

</body>
</html>
```